Marla Quint Memoir

Book Cover Design
Title: Cedars and Salt
Subtitle: One Girl's Climb Through Kinship and Mercy
Author: Marla Quint
Book Description: Marla Quint’s memoir Cedars and Salt, follows five generations of one Alaskan family evolving with the rapidly changing landscape of the North. Few memoirs combine love of nature with love of family so eloquently, while at the same time acknowledging that each carries the potential for so much loss and pain. Through it all, this is the story of one woman’s quest to carve a place for herself in a rapidly changing land and claim her own unique power.
INSTRUCTIONS: Open to any interesting creative designs reflecting the above description. However, MUST include the attached photo on the cover in some way. Have also attached the .indd template for reference. Please leave bleed area plus 1/2 inch all around. On spine, leave two inches at bottom to allow for publisher's logo.

```html
<!DOCTYPE html>
<html lang="en">
<head>
<meta charset="utf-8">
<title>Cedars and Salt — Marla Quint</title>
<link rel="stylesheet" href="https://fonts.googleapis.com/css2?family=Cinzel:wght@400;500&display=swap">
<style>
  :root {
    --page-bg: #ececec;
    --ice-light: #d6e6ef;
    --ice-mid: #a9c6d6;
    --ice-deep: #8fb1c5;
    --snow: #ffffff;
    --title-red: #6c1216;
    --ink: #1b1d20;
  }
  * { margin: 0; padding: 0; box-sizing: border-box; }
  html, body {
    width: 1200px;
    height: 924px;
    overflow: hidden;
    background: var(--page-bg);
  }
  .cover {
    position: absolute;
    left: 317px;
    top: 32px;
    width: 566px;
    height: 860px;
    overflow: hidden;
    font-family: "Cinzel", "Trajan Pro", serif;
    text-align: center;
    box-shadow: 0 6px 24px rgba(0,0,0,0.18);
  }
  .cover-photo {
    position: absolute;
    inset: 0;
    background:
      radial-gradient(ellipse 38% 30% at 50% 64%, #e6f0f5 0%, rgba(230,240,245,0) 100%),
      radial-gradient(ellipse 16% 14% at 48% 60%, #3a1614 0%, rgba(58,22,20,0) 100%),
      linear-gradient(160deg, var(--ice-light) 0%, var(--ice-mid) 55%, var(--ice-deep) 100%);
  }
  .title {
    position: absolute;
    left: 0;
    right: 0;
    top: 52px;
    font-weight: 500;
    line-height: 1;
  }
  .title-lead {
    display: block;
    font-size: 68px;
    color: var(--title-red);
    letter-spacing: -0.01em;
  }
  .title-main {
    display: block;
    margin-top: 4px;
    font-size: 205px;
    font-weight: 400;
    color: var(--snow);
    letter-spacing: -0.02em;
    line-height: 0.9;
  }
  .subtitle {
    position: absolute;
    left: 0;
    right: 0;
    top: 680px;
    font-size: 22px;
    line-height: 1.2;
    color: var(--ink);
    letter-spacing: 0.02em;
  }
  .author {
    position: absolute;
    left: 0;
    right: 0;
    top: 762px;
    font-size: 42px;
    color: var(--ink);
    letter-spacing: 0.16em;
  }
</style>
</head>
<body>
  <main class="cover">
    <div class="cover-photo" role="img" aria-label="Close-up photograph of a dark autumn leaf frozen into pale blue river ice, edged with frost crystals"></div>
    <h1 class="title">
      <span class="title-lead">CEDARS AND</span>
      <span class="title-main">SALT</span>
    </h1>
    <p class="subtitle">ONE GIRL'S CLIMB THROUGH<br>KINSHIP AND MERCY</p>
    <p class="author">MARLA QUINT</p>
  </main>
</body>
</html>
```